IT Company requires new Business Card design.

Over the years we have had a few different business card designs. We are now due for new cards across the board for all staff. We felt this would be a good time to start fresh with a new design. Our traditional card simply had our details on the front, and a list of services on the back. We don't particularly need the list of services, we have had cards where the only thing on the rear of the card was our logo.
Feel free to be creative, we would like our tag line "Complete IT Management" to appear at some point, doesn't necessarily have to be with the logo.
I have attached samples and drafts of various previous cards we have used over the years.
Industry/Entity Type
Business
Look and feel
Each slider illustrates characteristics of the customer's brand and the style your logo design should communicate.

```html
<!DOCTYPE html>
<html lang="en">
<head>
<meta charset="utf-8">
<title>Harbour Networking – Business Card</title>
<link href="https://fonts.googleapis.com/css2?family=Open+Sans:wght@400;600;800&display=swap" rel="stylesheet">
<style>
  :root{
    --slate:#5f7381;
    --slate-dark:#4d5f6b;
    --ink:#3a3f44;
    --paper:#ffffff;
    --stage:#e4e5ea;
    --rule:#b9bec3;
  }
  *{box-sizing:border-box;margin:0;padding:0}
  html,body{width:1200px;height:987px;overflow:hidden;background:var(--stage);font-family:"Open Sans",sans-serif}
  .canvas{position:relative;width:1200px;height:987px}
  .card{position:absolute;width:620px;height:379px;background:var(--paper);border-radius:30px;overflow:hidden;box-shadow:0 6px 18px rgba(0,0,0,.12)}
  .card--back{left:540px;top:80px}
  .card--front{left:60px;top:520px}

  /* back */
  .back-mark{position:absolute;left:0;right:0;top:130px;display:flex;justify-content:center;align-items:center;gap:16px;color:var(--slate);white-space:nowrap}
  .back-mark__square{width:30px;height:30px;background:var(--slate);flex:none}
  .back-mark__name{font-weight:800;font-size:38px;letter-spacing:1px;text-transform:uppercase}
  .back-web{position:absolute;left:0;right:0;bottom:70px;text-align:center;font-size:19px;letter-spacing:2px;color:var(--ink)}

  /* front */
  .wave{position:absolute;inset:0}
  .brand{position:absolute;left:40px;top:52px;color:var(--slate)}
  .brand__name{display:flex;align-items:center;gap:10px;font-weight:800;font-size:26px;line-height:1.05;text-transform:uppercase}
  .brand__square{width:20px;height:20px;background:var(--slate);flex:none}
  .brand__tag{margin-top:6px;margin-left:30px;font-size:10px;letter-spacing:2.6px;text-transform:uppercase;color:var(--slate)}
  .divider{position:absolute;left:298px;top:40px;width:1px;height:190px;background:linear-gradient(var(--rule),rgba(185,190,195,0))}
  .person{position:absolute;left:314px;top:44px;right:16px;color:var(--ink)}
  .person__name{font-weight:800;font-size:21px;color:var(--slate)}
  .person__role{font-size:16px;margin-bottom:12px}
  .contacts{list-style:none;font-size:15px;line-height:24px}
  .contacts li{display:flex;align-items:center;gap:8px;white-space:nowrap}
  .contacts svg{width:14px;height:14px;fill:var(--slate-dark);flex:none}
  .address{position:absolute;left:34px;top:250px;color:#fff;font-size:16px;line-height:23px;font-style:normal}
</style>
</head>
<body>
<main class="canvas">

  <section class="card card--back" aria-label="Card back">
    <div class="back-mark">
      <span class="back-mark__square"></span>
      <span class="back-mark__name">Harbour Networking</span>
    </div>
    <p class="back-web">www.harbournetworking.com.au</p>
  </section>

  <section class="card card--front" aria-label="Card front">
    <svg class="wave" viewBox="0 0 620 379" preserveAspectRatio="none" aria-hidden="true">
      <path d="M0 205 C150 200 250 250 330 310 S480 372 620 364 L620 379 L0 379 Z" fill="var(--slate)"/>
      <path d="M0 196 C150 190 255 242 335 302 S485 362 620 354" fill="none" stroke="var(--slate)" stroke-width="1.5"/>
      <path d="M0 190 C150 184 258 236 338 296 S488 355 620 347" fill="none" stroke="#c9cdd1" stroke-width="1"/>
    </svg>

    <div class="brand">
      <div class="brand__name"><span class="brand__square"></span><span>Harbour<br>Networking</span></div>
      <p class="brand__tag">Complete IT Management</p>
    </div>

    <div class="divider"></div>

    <div class="person">
      <p class="person__name">Daniel Reed</p>
      <p class="person__role">Operation Manager</p>
      <ul class="contacts">
        <li><svg viewBox="0 0 16 16"><path d="M3 1l3 3-2 2c1 2 3 4 5 5l2-2 3 3-2 3C6 14 2 10 1 3z"/></svg>08 9400 1188</li>
        <li><svg viewBox="0 0 16 16"><path d="M5 0h6a1 1 0 011 1v14a1 1 0 01-1 1H5a1 1 0 01-1-1V1a1 1 0 011-1zm1 2v6h4V2z"/></svg>0400 512 736</li>
        <li><svg viewBox="0 0 16 16"><path d="M4 1h6v4H4zM1 6h14v8H1zm3 2v2h8V8z"/></svg>08 9400 1188</li>
        <li><svg viewBox="0 0 16 16"><path d="M1 3h14v10H1zm1 1l6 5 6-5z"/></svg>daniel@harbournetworking.com.au</li>
        <li><svg viewBox="0 0 16 16"><path d="M8 1a7 7 0 100 14A7 7 0 008 1zm0 1.5c.9 1 1.5 3 1.6 4.8H6.4C6.5 5.5 7.1 3.5 8 2.5zM3 7.3a5 5 0 012.3-3.8A9 9 0 004.9 7.3zm0 1.4h1.9a9 9 0 00.4 3.8A5 5 0 013 8.7zm3.4 0h3.2c-.1 1.8-.7 3.8-1.6 4.8-.9-1-1.5-3-1.6-4.8zm4.7 0H13a5 5 0 01-2.3 3.8 9 9 0 00.4-3.8zm0-1.4a9 9 0 00-.4-3.8A5 5 0 0113 7.3z"/></svg>www.harbournetworking.com.au</li>
      </ul>
    </div>

    <address class="address">
      Unit 4 12 Marina Drive<br>Bayview WA 6000
    </address>
  </section>

</main>
</body>
</html>
```